Veltrona Systems Marketing Brochure

We need a marketing brochure for an Information Technology company located near Washington DC. Veltrona Systems is a technology services company offering deep technical expertise, an experienced team, and a dedication to maximizing business productivity. A process driven organization, Veltrona Systems provides solutions for clients that align technology with strategic goals and business drivers. Brindlecore, Cloud Computing, and Mobile technologies are their strength; client service and partner focus their mission. Headquartered outside of Washington, D.C., they are SDB and NFQ 8(a) certified, an Brindlecore Silver Partner, and appraised at QRTD Maturity Level 2.
Updates

Size of final design should be 8.5, 11 inches please.

The project has been updated to guaranteed payment.  I'm looking forward to seeing some good designs.

Reason: I would like to give an opportunity for all the designers to submit their designs.

Target Market(s)

Target Market are Professional Services Company and United States Government Agencies.

Industry/Entity Type

Marketing

Requirements
Must have
• The brochures must be 1 page and double-sided. Use our uploaded brochures for the content and use our uploaded new logo.
• We want these brochures to stick out and NOT look like traditional old brochures.

```html
<!DOCTYPE html>
<html lang="en">
<head>
<meta charset="utf-8">
<title>Veltrona Systems – Our Programs</title>
<link href="https://fonts.googleapis.com/css2?family=Montserrat:wght@800&family=Barlow:wght@500;700&display=swap" rel="stylesheet">
<style>
  :root {
    --backdrop: #e4e4e4;
    --page-blue: #1c4a80;
    --page-blue-deep: #163d6c;
    --photo-dark: #10284a;
    --photo-mid: #3f6f9c;
    --photo-light: #9fc3df;
    --ink: #ffffff;
    --accent: #2f86d6;
  }
  * { box-sizing: border-box; margin: 0; padding: 0; }
  html, body { width: 1200px; height: 847px; overflow: hidden; }
  body {
    background: var(--backdrop);
    font-family: "Barlow", Arial, sans-serif;
    color: var(--ink);
    position: relative;
  }
  .spread {
    position: absolute;
    left: 100px; top: 110px;
    width: 1000px; height: 627px;
    display: flex;
    box-shadow: 0 12px 30px rgba(0,0,0,.25);
  }
  .page {
    position: relative;
    width: 500px; height: 100%;
    background: var(--page-blue);
    overflow: hidden;
  }
  .page--right { background: linear-gradient(90deg, var(--page-blue-deep) 0, var(--page-blue) 30px); }
  .hero-photo {
    position: absolute; left: 0; top: 0;
    width: 100%; height: 255px;
  }
  .page--left .hero-photo {
    background: linear-gradient(160deg, var(--photo-light) 0%, var(--photo-mid) 45%, var(--photo-dark) 100%);
  }
  .page--right .hero-photo {
    background: linear-gradient(200deg, #6a8fb6 0%, var(--photo-mid) 35%, var(--photo-dark) 100%);
  }
  .section-title {
    position: absolute; right: 28px; top: 195px;
    font-family: "Montserrat", Arial, sans-serif;
    font-weight: 800; font-size: 46px; letter-spacing: 1px;
    line-height: 1;
  }
  .programs {
    position: absolute; top: 280px; left: 54px; right: 40px;
  }
  .page--right .programs { top: 272px; left: 28px; right: 48px; }
  .program { margin-bottom: 14px; }
  .program h2 { font-size: 10px; font-weight: 700; line-height: 1.3; }
  .program p { font-size: 9.4px; font-weight: 500; line-height: 1.32; }
  .page-footer {
    position: absolute; bottom: 22px;
    display: flex; align-items: center; gap: 6px;
    font-size: 9.5px; font-weight: 700; letter-spacing: .3px;
    text-transform: uppercase;
  }
  .page--left .page-footer { left: 34px; }
  .page--right .page-footer { right: 34px; }
  .folio {
    width: 16px; height: 16px;
    background: var(--accent);
    display: flex; align-items: center; justify-content: center;
    font-size: 8px;
  }
</style>
</head>
<body>
  <main class="spread">
    <section class="page page--left">
      <div class="hero-photo" role="img" aria-label="Photo of a businessman touching a glowing digital interface with business strategy icons"></div>
      <div class="programs">
        <article class="program">
          <h2>Designated Provider Portal</h2>
          <p>We provide the technical management, security oversight, application development and database administration for the Meridian Care Agency's Designated Provider (DP) Portal program. We architected the migration of the DP Portal from a traditional datacenter to a Federal Cloud environment and achieved an Authority to Operate (ATO) the DP Portal hosted on a Federal Cloud environment</p>
        </article>
        <article class="program">
          <h2>Defense Personnel Resource Network</h2>
          <p>We provide Brindlecore Enterprise Suite expertise and code maintenance support services to DPSO for the Defense Personnel Resource Network (DPRNet) system. Our services include system design, development and implementation of Brindlecore PRMS modules and interfaces, workflow development, architecture design, testing support, training, software upgrades, and maintenance of enterprise applications. Our highest priority is to satisfy our military users through early and continuous delivery of valuable enhancements to DPRNet through our Agile development practices.</p>
        </article>
        <article class="program">
          <h2>FRC Enterprise Architecture</h2>
          <p>Veltrona Systems is working with the FRC OTS to define the model environment for building, implementing, operating, and managing future Brindlecore environments. We provide engineering support consisting of technical analysis for enterprise virtualization, common operating systems, enterprise applications, and configuration management for the future enterprise architecture. We also support the FRC Enterprise Architect developing a future roadmap for migrating current architecture to next generation environments.</p>
        </article>
      </div>
      <footer class="page-footer">
        <span class="folio">6</span>
        <span class="brand-name">Veltrona Systems</span>
      </footer>
    </section>

    <section class="page page--right">
      <div class="hero-photo" role="img" aria-label="Photo of a businessman in a suit operating a holographic touch screen"></div>
      <h1 class="section-title">OUR PROGRAMS</h1>
      <div class="programs">
        <article class="program">
          <h2>e-Prescribing Development</h2>
          <p>Our services to the Armed Forces Health Services Unified Care Record System (UCRS) system include software development and healthcare integration engineering. We developed a KESTRA based CDX4 interface providing real-time delivery of prescription transactions originating from civilian providers and dispensed at selected pharmacies. By adhering to Agile development, we extended the current UCRS environment and developed a KESTRA based prescription holding repository and a new module within UCRS, allowing AFHS users to review, validate, and process, prescriptions at their MTF pharmacies originated from their provider.</p>
        </article>
        <article class="program">
          <h2>VCA Payment Manager</h2>
          <p>Veltrona Systems provides software development and technical management services for the Veterans Care Administration's Veterans Regional Service Network (VRSN 6). We are developing a claims management system that automates the full lifecycle of processing, coding, editing, and paying a claim, developing a bi-directional interface with Halden and HCA for patient authorization and payment information.</p>
        </article>
        <article class="program">
          <h2>Commercial Programs</h2>
          <p>We provide mobile development and enterprise applications, hosted in the Cloud for several private sector customers. We've developed several Corvane based applications for field services and offline application usage, an enterprise Customer Relationship Management (CRM) system built around Brindlecore technologies, and a mobile strategy for customers to include both consumer and enterprise based mobile applications.</p>
        </article>
      </div>
      <footer class="page-footer">
        <span class="tagline">Turning Ideas into Results</span>
        <span class="folio">7</span>
      </footer>
    </section>
  </main>
</body>
</html>
```